Stonebrook 720 Real Estate Investment Company

We need a business card designed for a real estate investment company named Stonebrook 720. We want to use red#f04a50, orange #f37122 and yellow #fbee3e as the color scheme. The logo colors will need to be modified from the current blue palette. I've attach VitaPathway logo example that captures the color scheme we're going for for Stonebrook 720. Looking for clean Sans Serif fonts.
Contact Information for Business Card
Daniel Furlow
Managing Partner
48317 Whitfield Lane, Suite 510
Tampa, FL 33718
813-555-4870 Mobile
dfurlow@stonebrook720.example
www.stonebrook720.example
Requirements
Must have
- Looking for creative responses.
Nice to have
- Must hit color palette... orange, red, yellow

```html
<!DOCTYPE html>
<html lang="en">
<head>
<meta charset="utf-8">
<title>Stonebrook 720 – Business Card</title>
<link rel="stylesheet" href="https://fonts.googleapis.com/css2?family=Montserrat:wght@400;500;800&display=swap">
<style>
  :root {
    --page: #e9e6e1;
    --paper: #f7f8fa;
    --ink: #050505;
    --yellow: #fbee3e;
    --orange: #f37122;
    --red: #f04a50;
    --wordmark: #3b3c3f;
    --light: #ffffff;
  }
  * { box-sizing: border-box; margin: 0; padding: 0; }
  html, body { width: 1200px; height: 795px; overflow: hidden; }
  body {
    background: var(--page);
    font-family: "Montserrat", Arial, sans-serif;
    position: relative;
  }
  .card {
    position: absolute;
    top: 237px;
    width: 560px;
    height: 320px;
    background: var(--paper);
    overflow: hidden;
    box-shadow: 0 6px 18px rgba(0,0,0,0.18);
  }
  .card--front { left: 27px; }
  .card--back { left: 613px; }

  .wordmark {
    position: absolute;
    display: flex;
    align-items: center;
    gap: 12px;
    white-space: nowrap;
  }
  .wordmark__name {
    font-weight: 800;
    color: var(--wordmark);
    font-size: 38px;
    letter-spacing: -0.5px;
  }
  .wordmark__dot {
    width: 22px; height: 22px;
    border-radius: 50%;
    background: var(--orange);
  }
  .card--front .wordmark { left: 92px; top: 62px; }
  .card--back .wordmark { left: 92px; top: 128px; }

  .front__band {
    position: absolute;
    left: 0; right: 0; top: 168px; bottom: 0;
    background: var(--ink);
  }
  .namebox {
    position: absolute;
    left: 0; top: 224px;
    width: 248px; height: 60px;
    background: var(--yellow);
    padding: 8px 0 0 30px;
    color: var(--ink);
  }
  .namebox__name { font-size: 23px; font-weight: 500; line-height: 1.1; }
  .namebox__title { font-size: 12.5px; font-weight: 500; letter-spacing: 0.3px; }

  .contact {
    position: absolute;
    left: 290px; top: 188px;
    list-style: none;
    color: var(--light);
    font-size: 10.5px;
    line-height: 1.3;
  }
  .contact::before {
    content: "";
    position: absolute;
    left: 8px; top: 10px; bottom: 12px;
    width: 1px;
    background: var(--yellow);
  }
  .contact__item {
    position: relative;
    display: flex;
    align-items: center;
    gap: 12px;
    min-height: 26px;
  }
  .contact__icon {
    flex: none;
    width: 17px; height: 17px;
    border-radius: 50%;
    background: var(--yellow);
    display: flex; align-items: center; justify-content: center;
    position: relative;
  }
  .contact__icon svg { width: 10px; height: 10px; }

  .back__stripe { position: absolute; left: 0; right: 0; }
  .back__stripe--top-dark { top: 0; height: 28px; background: var(--ink); }
  .back__stripe--top-accent { top: 28px; height: 20px; background: var(--yellow); }
  .back__stripe--bottom-accent { bottom: 40px; height: 20px; background: var(--yellow); }
  .back__stripe--bottom-dark { bottom: 0; height: 40px; background: var(--ink); }
</style>
</head>
<body>
  <section class="card card--front" aria-label="Business card front">
    <div class="wordmark">
      <span class="wordmark__name">Stonebrook 720</span>
      <span class="wordmark__dot"></span>
    </div>
    <div class="front__band"></div>
    <div class="namebox">
      <p class="namebox__name">Daniel Furlow</p>
      <p class="namebox__title">Managing Partner</p>
    </div>
    <ul class="contact">
      <li class="contact__item">
        <span class="contact__icon"><svg viewBox="0 0 10 10"><path d="M5 0.5a3.2 3.2 0 0 0-3.2 3.2C1.8 6 5 9.5 5 9.5S8.2 6 8.2 3.7A3.2 3.2 0 0 0 5 0.5zm0 4.4a1.2 1.2 0 1 1 0-2.4 1.2 1.2 0 0 1 0 2.4z" fill="#050505"/></svg></span>
        <span>48317 Whitfield Lane, Suite 510<br>Tampa, FL 33718</span>
      </li>
      <li class="contact__item">
        <span class="contact__icon"><svg viewBox="0 0 10 10"><path d="M2.2 0.8l1.6 1.9-0.9 1.1c0.6 1.3 1.6 2.3 2.9 2.9l1.1-0.9 1.9 1.6-0.9 1.3C4.6 8.6 1.4 5.4 0.9 2.1z" fill="#050505"/></svg></span>
        <span>813-555-4870 Mobile</span>
      </li>
      <li class="contact__item">
        <span class="contact__icon"><svg viewBox="0 0 10 10"><rect x="1" y="2.2" width="8" height="5.6" fill="none" stroke="#050505" stroke-width="1"/><path d="M1 2.4l4 3 4-3" fill="none" stroke="#050505" stroke-width="1"/></svg></span>
        <span>dfurlow@stonebrook720.example</span>
      </li>
      <li class="contact__item">
        <span class="contact__icon"><svg viewBox="0 0 10 10"><circle cx="5" cy="5" r="3.8" fill="none" stroke="#050505" stroke-width="1"/><path d="M1.2 5h7.6M5 1.2c-2 2.4-2 5.2 0 7.6M5 1.2c2 2.4 2 5.2 0 7.6" fill="none" stroke="#050505" stroke-width="0.8"/></svg></span>
        <span>www.stonebrook720.example</span>
      </li>
    </ul>
  </section>

  <section class="card card--back" aria-label="Business card back">
    <div class="back__stripe back__stripe--top-dark"></div>
    <div class="back__stripe back__stripe--top-accent"></div>
    <div class="wordmark">
      <span class="wordmark__name">Stonebrook 720</span>
      <span class="wordmark__dot"></span>
    </div>
    <div class="back__stripe back__stripe--bottom-accent"></div>
    <div class="back__stripe back__stripe--bottom-dark"></div>
  </section>
</body>
</html>
```